Engineering Land Development Company Needs Flyer Brochure for Prospective Professional Clients

Our company provides land development site design for commercial projects. We have many repeat clients that are familiar with our work. We do not advertise our services other than a website. Most of our referrals are from existing clients. When a new client contacts us and asks for a proposal for a project we would like to have a brochure that shows our strengths, experience, and professionalism. We are selling professional services similar to a lawyer or accountant. We want new clients to feel comfortable hiring a new firm. The brochure would be one page single-side included when we submit proposals for new projects. Check out our website at tovamrk.net for more info. We would like a brochure that mixes grading/excavation construction work on a job site with business professional. We will need to update the brochure so we want it in .doc .psd or some other edit format. The brochure we are using is attached. It is very two-dimensional. We need some depth.

Target Market(s)

Land developers, architects, real estate, professionals, attorneys

Industry/Entity Type

Real Estate Development

Font styles to use
Sans Serif
Other font styles liked:
• calibri

Colors
0355a3
9bcb3c

Requirements
Must have
• company logo, ability to update text and images
Nice to have
• background image(s) with text overlay
Should not have
• cartoons, harsh colors, stock photos of people, lots of boxes

```html
<!DOCTYPE html>
<html lang="en">
<head>
<meta charset="utf-8">
<title>Tovamark Engineering – Services Flyer</title>
<link href="https://fonts.googleapis.com/css2?family=Arimo:ital,wght@0,400;0,700;1,700&display=swap" rel="stylesheet">
<style>
:root{
  --brand-blue:#0355a3;
  --heading-blue:#4a55b8;
  --brand-green:#9bcb3c;
  --bright-green:#3fbf3a;
  --ink:#1c1c1c;
  --body-ink:#333;
  --stage:#e4e7ea;
  --paper-top:#ffffff;
  --paper-bottom:#e9ecee;
}
*{box-sizing:border-box;margin:0;padding:0}
html,body{width:1200px;height:797px;overflow:hidden}
body{background:var(--stage);font-family:"Arimo",Arial,sans-serif;color:var(--ink);position:relative}
.flyer{position:absolute;left:320px;top:36px;width:560px;height:725px;
  background:linear-gradient(180deg,var(--paper-top) 0%,var(--paper-bottom) 64%);
  box-shadow:0 6px 22px rgba(0,0,0,.18);overflow:hidden}
.client-strip{height:30px;display:flex;align-items:center;justify-content:space-between;padding:0 10px;gap:4px}
.client-name{font-size:6.6px;font-weight:700;color:var(--brand-blue);white-space:nowrap;display:flex;align-items:center;gap:2px}
.client-name i{display:inline-block;width:5px;height:5px;border-radius:50%;background:var(--brand-blue)}
.accent-band{height:9px;background:linear-gradient(90deg,var(--bright-green),var(--brand-green))}
.featured-client{position:absolute;right:22px;top:48px;font-size:11px;font-weight:700;color:#6a2c91;display:flex;align-items:center;gap:4px}
.featured-client i{width:12px;height:12px;border-radius:50%;background:#6a2c91;display:inline-block}
.mission{margin:16px 100px 0 70px;text-align:center;font-size:18px;font-weight:700;line-height:1.15;color:var(--heading-blue)}
.intro{position:absolute;left:22px;top:128px;width:330px;font-size:14.5px;line-height:1.2;color:var(--ink)}
.site-photo{position:absolute;left:372px;top:118px;width:168px;height:92px;border:3px solid var(--bright-green);border-radius:12px;
  background:linear-gradient(180deg,#8cc0e6 0%,#b9d7ea 38%,#d3a16b 62%,#c9834a 100%)}
.services{position:absolute;left:22px;top:200px;width:520px}
.service{margin-bottom:8px}
.service h2{font-size:15px;font-weight:700;letter-spacing:.5px;color:var(--heading-blue);line-height:1.05}
.service h3{font-size:10.5px;font-weight:400;color:var(--bright-green);line-height:1.15}
.service p{font-size:6.6px;line-height:1.35;color:var(--body-ink);margin-top:1px}
.equipment-partner{position:absolute;right:22px;top:372px;font-size:8px;font-weight:700;color:#2d7a2d;display:flex;align-items:center;gap:3px}
.equipment-partner i{width:10px;height:10px;background:#f2c300;display:inline-block}
.project-photo{position:absolute;left:0;right:0;bottom:0;height:250px;
  background:linear-gradient(180deg,#5c6f8f 0%,#8d98a8 30%,#6f6258 62%,#8a6a4c 100%)}
.contact{position:absolute;left:22px;bottom:18px;font-size:14px;line-height:1.2;color:var(--bright-green);font-weight:700}
.firm-mark{position:absolute;right:20px;bottom:24px;display:flex;align-items:center;gap:6px;color:#fff;font-size:11px;font-weight:700}
.firm-mark i{width:22px;height:22px;border-radius:50%;background:#7c6bc4;display:inline-block}
</style>
</head>
<body>
<main class="flyer">
  <header>
    <div class="client-strip">
      <span class="client-name"><i></i>Corvent</span>
      <span class="client-name">Grocer Vale</span>
      <span class="client-name">Pancake Row</span>
      <span class="client-name">Benchmark Supply</span>
      <span class="client-name">Toastline</span>
      <span class="client-name">Partsway</span>
      <span class="client-name">Meridian Motors</span>
      <span class="client-name">Fieldgate Foods</span>
      <span class="client-name">Flapwing Grill</span>
      <span class="client-name">Crustory</span>
      <span class="client-name">Salsa Fold</span>
      <span class="client-name">Pawcart</span>
    </div>
    <div class="accent-band"></div>
  </header>

  <div class="featured-client"><i></i>Bellamesa</div>

  <h1 class="mission">Our mission at Tovamark Engineering is to provide Superior Quality Professional Land Development Services</h1>

  <p class="intro">Our business would not be successful with out the support of our clients. Some of our project clients include:</p>

  <div class="site-photo" role="img" aria-label="Excavator digging red clay on a job site under a blue sky"></div>

  <section class="services">
    <article class="service">
      <h2>PLANNING</h2>
      <h3>We are land development professionals who can see the “big picture”.</h3>
      <p>We have extensive experience with site selection, due diligence investigations, re-zonings, and land planning. Every project is different. We look forward to identifying all feasible alternatives. We become part of the project and enjoy developing the best plan for the success of each particular project. We understand that time is money and unexpected delays are unacceptable.</p>
    </article>
    <article class="service">
      <h2>SURVEYING</h2>
      <h3>We are land development professionals who provide superior quality surveying services.</h3>
      <p>Our firm can handle any surveying need. We have extensive experience with ALTA surveys, boundary surveys, subdivision platting, topographic/location surveys, GPS surveys, R/W surveys, construction staking, as-built surveys, elevation certificates, etc. We work closely with title attorneys to provide legal descriptions, exhibits, and other assistance when closing the real estate deal.</p>
    </article>
    <article class="service">
      <h2>ENGINEERING</h2>
      <h3>We are land development professionals who can handle the most complicated engineering challenge.</h3>
      <p>Let us worry about all the technical stuff and the regulators. Our firm has extensive experience with infrastructure assessments, erosion control, grading, roadway design, stormwater management, water systems, sewer systems, utilities, flood plain management, landscape design, permitting, bidding, and construction administration.</p>
    </article>
    <article class="service">
      <h2>ENVIRONMENTAL</h2>
      <h3>We are land development professionals who provide superior quality environmental services.</h3>
      <p>We provide environmental site assessments, underground storage tank management, soil and groundwater sampling and testing, contamination remediation, Brownfields assessments, permitting and redevelopment, and wetlands permitting. Our firm works closely with state and federal agencies to provide economical mitigation and remediation solutions.</p>
    </article>
  </section>

  <div class="equipment-partner"><i></i>Furrow Tractor</div>

  <footer class="project-photo" role="img" aria-label="Steel frame of a large commercial building under construction on a graded site">
    <address class="contact">
      (555) 014-2290<br>
      www.tovamrk.net<br>
      Fairhaven, NC 28000<br>
      410 Ridgeline Avenue, Suite 12
    </address>
    <div class="firm-mark"><i></i>Tovamark Engineering PLLC</div>
  </footer>
</main>
</body>
</html>
```